Budget planning & tracking app

I want to make personal budget planning and tracking easier and more enjoyable for people from all walks of life. I will aim to assist students, graduates, young professionals and anyone else interested, to get a grip on their personal finances early-on in life, allowing them to build their wealth plan to retirement, and also giving them an easy way to track their financial performance. I want to develop an intuative app that will make capturing daily transaction details a seamless and easy process.

Target Market(s)

This app must appeal to anyone in need of an easy and intuative solution to track their daily finances and to understand what their current lifestyle will mean for their wealth building..

Industry/Entity Type

Personal finance

Font styles to use
Sans Serif

Requirements
Must have
• Super easy and intuative interface, easy capturing of actual expenses, easy setup of planned income and expenses, visual representation of wealth building over time.
Nice to have
• Would be nice if there's.some way to present the solution in a gaming interface, so capturing daily expenses feels less like a chore and more like a game.
Should not have
• Should not look like a spreadsheet.

```html
<!DOCTYPE html>
<html lang="en">
<head>
<meta charset="utf-8">
<title>Budget Planner – Home</title>
<link href="https://fonts.googleapis.com/css2?family=Inter:wght@300;400;500;600;700;800&display=swap" rel="stylesheet">
<style>
  :root {
    --header-blue: #7b9ffc;
    --strip-dark: #3d4a6e;
    --strip-mid: #5b6c98;
    --tab-active: #6287e6;
    --tab-idle: #8ea6dc;
    --card-light: #9fbcfb;
    --btn-light: #7a9cf2;
    --btn-dark: #3b5ca8;
    --amount-top: #a7c1fc;
    --amount-bottom: #80a2fb;
    --ink: #1c1f26;
    --white: #ffffff;
    --soft-white: #e6edff;
    --page: #ffffff;
  }
  * { box-sizing: border-box; margin: 0; padding: 0; }
  html, body { width: 1200px; height: 2412px; overflow: hidden; background: var(--page); }
  body { font-family: "Inter", sans-serif; color: var(--white); position: relative; }

  .header { position: absolute; left: 0; top: 0; width: 1200px; height: 622px; background: var(--header-blue); }
  .greeting { position: absolute; left: 98px; top: 110px; font-size: 66px; font-weight: 700; }
  .limit-amount { position: absolute; left: 0; width: 100%; top: 300px; text-align: center; font-size: 176px; font-weight: 800; letter-spacing: -2px; line-height: 1.15; }
  .limit-caption { position: absolute; left: 0; width: 100%; top: 508px; text-align: center; font-size: 34px; font-weight: 300; color: var(--soft-white); }

  .strip { position: absolute; left: 0; width: 1200px; display: flex; align-items: center; white-space: nowrap; overflow: hidden; font-size: 37px; font-weight: 400; color: var(--soft-white); }
  .strip span { flex: none; }
  .strip .current { font-weight: 700; color: var(--white); }
  .date-strip { gap: 44px; }
  .date-strip .lead { margin-left: -60px; }
  .date-strip--top { top: 622px; height: 112px; background: var(--strip-dark); }
  .date-strip--bottom { top: 1597px; height: 110px; background: var(--strip-mid); }
  .category-strip { top: 1481px; height: 116px; background: var(--strip-dark); gap: 52px; }
  .category-strip .lead { margin-left: -34px; }
  .category-strip .current { margin: 0 40px; }

  .entry-tabs { position: absolute; left: 0; top: 734px; width: 1200px; height: 126px; display: flex; border-radius: 0 0 40px 40px; overflow: hidden; }
  .entry-tab { flex: 1; display: flex; align-items: center; justify-content: center; font-size: 68px; font-weight: 500; }
  .entry-tab--expense { background: var(--tab-active); flex: 0 0 598px; }
  .entry-tab--income { background: var(--tab-idle); }

  .section-title { position: absolute; left: 0; width: 100%; text-align: center; font-size: 44px; font-weight: 600; color: var(--ink); }
  .section-title--budget { top: 943px; }
  .section-title--quick { top: 1383px; }

  .budget-card { position: absolute; background: var(--card-light); border-radius: 34px; overflow: hidden; display: flex; flex-direction: column; }
  .budget-card__body { flex: 1; display: flex; flex-direction: column; align-items: center; justify-content: center; }
  .budget-card__actions { display: flex; height: 72px; }
  .budget-card__actions span { flex: 1; display: flex; align-items: center; justify-content: center; font-size: 36px; font-weight: 500; }
  .btn-change { background: var(--btn-light); }
  .btn-pay { background: var(--btn-dark); }
  .budget-card__title { font-size: 38px; font-weight: 400; display: flex; align-items: baseline; gap: 18px; }
  .budget-card__title b { font-size: 44px; font-weight: 700; }
  .budget-card__date { font-size: 27px; font-weight: 400; margin-top: 2px; }

  .budget-card--main { left: 315px; top: 1020px; width: 570px; height: 303px; }
  .budget-card--side { top: 1059px; width: 410px; height: 235px; }
  .budget-card--side .budget-card__actions { height: 56px; }
  .budget-card--side .budget-card__actions span { font-size: 26px; }
  .budget-card--side .budget-card__title { font-size: 24px; gap: 12px; }
  .budget-card--side .budget-card__title b { font-size: 26px; }
  .budget-card--side .budget-card__date { font-size: 18px; }
  .budget-card--left { left: -110px; }
  .budget-card--right { left: 900px; }

  .amount-panel { position: absolute; left: 0; top: 1822px; width: 1200px; height: 300px; border-radius: 40px; overflow: hidden; }
  .amount-panel__value { height: 145px; background: var(--amount-top); display: flex; align-items: center; justify-content: center; font-size: 90px; font-weight: 700; }
  .amount-panel__note { height: 155px; background: var(--amount-bottom); padding: 14px 0 0 331px; font-size: 34px; font-weight: 300; color: var(--soft-white); }

  .add-button { position: absolute; left: 315px; top: 2141px; width: 570px; height: 84px; border-radius: 42px; background: var(--btn-dark); display: flex; align-items: center; justify-content: center; font-size: 37px; font-weight: 700; letter-spacing: 1px; }
</style>
</head>
<body>
  <header class="header">
    <h1 class="greeting">Hi John Doe</h1>
    <div class="limit-amount">$ 125</div>
    <p class="limit-caption">Spend Limit for 2024-10-10</p>
  </header>

  <nav class="strip date-strip date-strip--top">
    <span class="lead">Sep 06</span><span>Sep 07</span><span>Sep 08</span><span>Sep 09</span><span class="current">Sep 10</span><span>Sep 11</span><span>Sep 12</span><span>Sep 10</span><span>Sep 14</span>
  </nav>

  <div class="entry-tabs">
    <div class="entry-tab entry-tab--expense">New Expenses</div>
    <div class="entry-tab entry-tab--income">New Income</div>
  </div>

  <h2 class="section-title section-title--budget">Planed Budget</h2>

  <article class="budget-card budget-card--side budget-card--left">
    <div class="budget-card__body" style="padding-left:90px">
      <svg width="52" height="52" viewBox="0 0 24 24" aria-hidden="true"><path fill="#fff" d="M6.6 10.8a15.1 15.1 0 0 0 6.6 6.6l2.2-2.2a1 1 0 0 1 1-.25 11.4 11.4 0 0 0 3.6.57 1 1 0 0 1 1 1V20a1 1 0 0 1-1 1A17 17 0 0 1 3 4a1 1 0 0 1 1-1h3.5a1 1 0 0 1 1 1c0 1.25.2 2.45.57 3.57a1 1 0 0 1-.25 1z"/></svg>
      <div class="budget-card__title" style="margin-top:18px">Phone Bill <b>$ 5 –</b></div>
    </div>
    <div class="budget-card__actions"><span class="btn-change">Change</span><span class="btn-pay">Pay Now</span></div>
  </article>

  <article class="budget-card budget-card--main">
    <div class="budget-card__body">
      <svg width="120" height="97" viewBox="0 0 68 55" aria-hidden="true">
        <path d="M20 22 L30 4 M48 22 L38 4" stroke="#fff" stroke-width="5" stroke-linecap="round" fill="none"/>
        <rect x="2" y="20" width="64" height="9" rx="3" fill="#fff"/>
        <path d="M7 31 H61 L56 53 H12 Z" fill="#fff"/>
        <path d="M22 36 V48 M34 36 V48 M46 36 V48" stroke="#9fbcfb" stroke-width="4" stroke-linecap="round"/>
      </svg>
      <div class="budget-card__title" style="margin-top:10px">Grocery <b>$ 15 +</b></div>
      <div class="budget-card__date">2024-10-10</div>
    </div>
    <div class="budget-card__actions"><span class="btn-change">Change</span><span class="btn-pay">Pay Now</span></div>
  </article>

  <article class="budget-card budget-card--side budget-card--right">
    <div class="budget-card__body" style="align-items:flex-start;padding-left:100px">
      <svg width="52" height="52" viewBox="0 0 24 24" aria-hidden="true" style="margin-left:38px"><path fill="#fff" d="M6.6 10.8a15.1 15.1 0 0 0 6.6 6.6l2.2-2.2a1 1 0 0 1 1-.25 11.4 11.4 0 0 0 3.6.57 1 1 0 0 1 1 1V20a1 1 0 0 1-1 1A17 17 0 0 1 3 4a1 1 0 0 1 1-1h3.5a1 1 0 0 1 1 1c0 1.25.2 2.45.57 3.57a1 1 0 0 1-.25 1z"/></svg>
      <div class="budget-card__title" style="margin-top:18px">Phone Bill <b>$ 5 –</b></div>
      <div class="budget-card__date">2024-10-10</div>
    </div>
    <div class="budget-card__actions"><span class="btn-change">Change</span><span class="btn-pay">Pay Now</span></div>
  </article>

  <h2 class="section-title section-title--quick">Quick Expenses</h2>

  <nav class="strip category-strip">
    <span class="lead">Food</span><span>Transport</span><span>Education</span><span class="current">Grocery</span><span>Savings &amp; investments</span>
  </nav>

  <nav class="strip date-strip date-strip--bottom">
    <span class="lead">Sep 06</span><span>Sep 07</span><span>Sep 08</span><span>Sep 09</span><span class="current">Sep 10</span><span>Sep 11</span><span>Sep 12</span><span>Sep 10</span><span>Sep 14</span>
  </nav>

  <section class="amount-panel">
    <div class="amount-panel__value">$ 15</div>
    <div class="amount-panel__note">Note :</div>
  </section>

  <div class="add-button">ADD NOW</div>
</body>
</html>
```